Tall Pines Oils

Need new label designs for the beard oils. I have three beard oil flavors currently
Colour themes are (red, green, and brown). Want to rid the different colour lines an keep it simple. Gold Black and white are colours i want to see for all.
Need a new look for the Beard Oil sticker for all three. No colours distinguishing flavours. Just one set colour for the font.

And a female one. (For female line). bottles same size. Only this will be a body oil.
Adding a female line so want the bottles to look similar in design but pink border for the female line. The only bottle that will have a colour pop.

Looking at having the designs in gold black and white only. The horse in the middle changed to gold.

Female bottle: Font saying "PURE DRIFT"
Male: Beard Oil

Again colours simplified to just three (gold black and white). Only female one with line of pink.

thanks

Target Market(s)

Bearded men, barbers, females

Industry/Entity Type

Cosmetic

Requirements
Nice to have
• Try removing the red colour of the horse and just have that in gold too
• Female font clear and simple

```html
<!DOCTYPE html>
<html lang="en">
<head>
<meta charset="UTF-8">
<title>Tall Pines Co. — Oil Labels</title>
<link href="https://fonts.googleapis.com/css2?family=Josefin+Sans:wght@300;400&family=Montserrat:wght@400;600&family=Marcellus&display=swap" rel="stylesheet">
<style>
  :root {
    --backdrop: #d4d4d4;
    --paper: #ffffff;
    --ink: #111111;
    --pink: #f364a2;
    --gold: #c9990a;
  }
  * { margin: 0; padding: 0; box-sizing: border-box; }
  html, body {
    width: 1200px;
    height: 696px;
    overflow: hidden;
  }
  body {
    background: var(--backdrop);
    display: flex;
    align-items: center;
    justify-content: center;
    gap: 80px;
  }
  .label {
    --accent: var(--pink);
    position: relative;
    width: 340px;
    height: 420px;
    background: var(--paper);
    border-top: 8px solid var(--accent);
    display: flex;
    flex-direction: column;
    align-items: center;
  }
  .label--beard { --accent: var(--gold); }
  .badge {
    background: var(--accent);
    color: var(--paper);
    font-family: "Montserrat", sans-serif;
    font-weight: 600;
    font-size: 15px;
    letter-spacing: 1px;
    padding: 4px 18px 5px;
    border-radius: 0 0 5px 5px;
  }
  .brand {
    margin-top: 96px;
    height: 40px;
    display: flex;
    align-items: center;
    gap: 10px;
    font-family: "Montserrat", sans-serif;
    font-weight: 600;
    font-size: 20px;
    color: var(--ink);
    letter-spacing: 0.5px;
  }
  .brand__dot {
    width: 14px;
    height: 14px;
    border-radius: 50%;
    background: var(--gold);
  }
  .band {
    margin-top: 40px;
    width: 100%;
    height: 120px;
    background: var(--accent);
    display: flex;
    flex-direction: column;
    align-items: center;
    justify-content: center;
    color: var(--paper);
  }
  .band__title {
    font-family: "Josefin Sans", sans-serif;
    font-weight: 300;
    font-size: 34px;
    letter-spacing: 4px;
    line-height: 1;
  }
  .label--beard .band__title { font-weight: 400; }
  .band__rule {
    width: 262px;
    height: 2px;
    background: var(--paper);
    margin: 14px 0 12px;
  }
  .band__subtitle {
    font-family: "Marcellus", serif;
    font-size: 18px;
    letter-spacing: 3px;
  }
  .size {
    margin-top: 22px;
    font-family: "Montserrat", sans-serif;
    font-size: 14px;
    color: var(--ink);
    letter-spacing: 1px;
  }
</style>
</head>
<body>
  <section class="label label--body">
    <div class="badge">100% NATURAL</div>
    <div class="brand"><span class="brand__dot"></span>TALL PINES CO.</div>
    <div class="band">
      <h1 class="band__title">PURE DRIFT</h1>
      <div class="band__rule"></div>
      <p class="band__subtitle">BODY OIL</p>
    </div>
    <p class="size">1 OZ</p>
  </section>

  <section class="label label--beard">
    <div class="badge">100% NATURAL</div>
    <div class="brand"><span class="brand__dot"></span>TALL PINES CO.</div>
    <div class="band">
      <h1 class="band__title">BEARD OIL</h1>
      <div class="band__rule"></div>
      <p class="band__subtitle">CEDAR TRAIL</p>
    </div>
    <p class="size">1 OZ</p>
  </section>
</body>
</html>
```